Business card for utility of the future

I need a business card template designed for brookvane. We provide sustainable water, energy and waste services to homes.

The card should include name, position, email address, phone number, website and our logo (attached). I would like it to convey professionalism and creativity.

Target Market(s)

Homeowners, investors, corporate partners.

Industry/Entity Type

Utility

Contact Information for Business Card

The card should include name, position, email address, phone number, website and our logo (attached).

```html
<!DOCTYPE html>
<html lang="en">
<head>
<meta charset="utf-8">
<title>brookvane business card</title>
<link href="https://fonts.googleapis.com/css2?family=Open+Sans:wght@400;600;700&display=swap" rel="stylesheet">
<style>
  :root {
    --green: #6cbd85;
    --orange: #ec8a64;
    --ink: #333333;
    --paper: #ffffff;
    --backdrop: #e8e5e0;
  }
  * { margin: 0; padding: 0; box-sizing: border-box; }
  html, body {
    width: 1200px; height: 1000px; overflow: hidden;
    background: var(--backdrop);
    font-family: "Open Sans", Arial, sans-serif;
  }
  .canvas { position: relative; width: 1200px; height: 1000px; }
  .card {
    position: absolute; left: 266px; width: 666px; height: 397px;
    border-radius: 22px; overflow: hidden;
    box-shadow: 0 6px 14px rgba(0,0,0,0.18);
  }
  .card--front { top: 74px; background: var(--paper); }
  .card--back { top: 533px; background: var(--green); }

  .wordmark {
    position: absolute; font-weight: 700; letter-spacing: -0.01em; line-height: 1;
    white-space: nowrap;
  }
  .card--front .wordmark { left: 52px; top: 166px; font-size: 47px; color: var(--green); }
  .card--back .wordmark { left: 0; right: 0; top: 150px; text-align: center; font-size: 72px; color: var(--paper); }

  .divider {
    position: absolute; left: 360px; top: 104px; width: 2px; height: 190px;
    background: linear-gradient(to bottom, rgba(108,189,133,0), var(--green) 35%, var(--green) 65%, rgba(108,189,133,0));
  }
  .details { position: absolute; left: 413px; top: 90px; color: var(--ink); }
  .details__name { font-size: 20px; font-weight: 600; color: var(--green); letter-spacing: 0.03em; line-height: 26px; }
  .details__role { font-size: 16px; color: var(--orange); line-height: 20px; }
  .details__address { margin-top: 15px; font-size: 16px; line-height: 22px; }
  .details__contacts { margin-top: 14px; list-style: none; }
  .details__contacts li { display: flex; align-items: center; font-size: 16px; line-height: 23.5px; }
  .details__contacts svg { width: 14px; height: 14px; margin-right: 7px; fill: var(--green); flex: none; }

  .card__wave { position: absolute; left: 0; bottom: 0; width: 666px; height: 397px; }
</style>
</head>
<body>
<div class="canvas">
  <section class="card card--front">
    <div class="wordmark">brookvane</div>
    <div class="divider"></div>
    <div class="details">
      <p class="details__name">SOREN ALDBERG</p>
      <p class="details__role">Founder</p>
      <p class="details__address">2415 Harlow Creek Rd,<br>Fairmont, MD 21304</p>
      <ul class="details__contacts">
        <li><svg viewBox="0 0 16 16"><path d="M1 6c0-2 3-3 7-3s7 1 7 3v1h-4V5.5H5V7H1z"/><path d="M3 8h10l1 5H2z"/></svg>+ 000 000 0000</li>
        <li><svg viewBox="0 0 16 16"><rect x="4" y="1" width="8" height="4"/><rect x="1" y="6" width="14" height="6" rx="1"/><rect x="4" y="10" width="8" height="5"/></svg>+ 000 000 0000</li>
        <li><svg viewBox="0 0 16 16"><path d="M1 3h14v1.5L8 9 1 4.5z"/><path d="M1 6l7 4.5L15 6v7H1z"/></svg>info@brookvane.com</li>
        <li><svg viewBox="0 0 16 16"><circle cx="8" cy="8" r="7"/><path d="M8 1v14M1 8h14" stroke="#fff" stroke-width="1" fill="none"/></svg>www.brookvane.com</li>
      </ul>
    </div>
    <svg class="card__wave" viewBox="0 0 666 397" aria-hidden="true">
      <path d="M0 349 Q333 420 666 349 L666 397 L0 397 Z" fill="var(--green)"/>
    </svg>
  </section>

  <section class="card card--back">
    <div class="wordmark">brookvane</div>
  </section>
</div>
</body>
</html>
```